RICE AND RUN WALL POSTER

Hi designer,

I would like to create a poster to put on my wall.

My intention is to place a bicycle onto a wall and have these words vinyl stick next to it.

" Life is not a race.
It is a journey
Enjoy each moment. Relax!
Have a bowl of Rice and Run
Make all your dreams come true "

I like traditional fonts - easy to read. See example. This is something I would love.

It will be on a white wall so black text would be ok. I have also attached my logo - maybe try include Rice and Run font in your design if possible - but not important.

Good luck everyone.

Font styles to use
Decorative
Script

Requirements
Must have
• The placement of my bike will be on the top left corner of the wall so I think it will be best fit if all designs are done in horizontal rectangular shape (landscape)

```html
<!DOCTYPE html>
<html lang="en">
<head>
<meta charset="utf-8">
<title>Rice and Run Wall Poster</title>
<link rel="stylesheet" href="https://fonts.googleapis.com/css2?family=Montserrat:wght@900&display=swap">
<style>
  :root {
    --paper: #ffffff;
    --ink: #0a0a0a;
    --badge-text: #ffffff;
  }
  html, body {
    margin: 0;
    padding: 0;
    width: 848px;
    height: 1200px;
    overflow: hidden;
    background: var(--paper);
  }
  .poster {
    display: block;
    width: 848px;
    height: 1200px;
  }
  .poster-line {
    font-family: "Montserrat", Arial, sans-serif;
    font-weight: 900;
    fill: var(--ink);
  }
  .brand-badge { fill: var(--ink); }
  .brand-name {
    font-family: "Montserrat", Arial, sans-serif;
    font-weight: 900;
    fill: var(--badge-text);
  }
</style>
</head>
<body>
<svg class="poster" viewBox="0 0 848 1200" xmlns="http://www.w3.org/2000/svg" role="img" aria-label="Life is not a race. It is a journey. Enjoy each moment. Relax! Have a bowl of Rice and Run. Make all your dreams come true.">
  <g class="quote-landscape">
    <g class="column column-left">
      <text class="poster-line" x="24" y="470" font-size="100" textLength="228" lengthAdjust="spacingAndGlyphs">LIFE</text>
      <text class="poster-line" x="262" y="438" font-size="40" textLength="142" lengthAdjust="spacingAndGlyphs">is not</text>
      <text class="poster-line" x="262" y="470" font-size="40" textLength="142" lengthAdjust="spacingAndGlyphs">a race.</text>
      <text class="poster-line" x="154" y="520" font-size="36" textLength="124" lengthAdjust="spacingAndGlyphs">It is a</text>
      <text class="poster-line" x="24" y="600" font-size="80" textLength="380" lengthAdjust="spacingAndGlyphs">JOURNEY</text>
      <text class="poster-line" x="24" y="655" font-size="37" textLength="380" lengthAdjust="spacingAndGlyphs">Enjoy each moment.</text>
      <text class="poster-line" x="24" y="750" font-size="88" textLength="380" lengthAdjust="spacingAndGlyphs">RELAX!</text>
    </g>

    <g class="column column-right">
      <text class="poster-line" x="444" y="458" font-size="58" textLength="238" lengthAdjust="spacingAndGlyphs">Have a</text>
      <text class="poster-line" x="444" y="528" font-size="58" textLength="240" lengthAdjust="spacingAndGlyphs">Bowl of</text>
      <text class="poster-line" x="444" y="600" font-size="52" textLength="380" lengthAdjust="spacingAndGlyphs">Make all your</text>
      <text class="poster-line" x="444" y="682" font-size="82" textLength="380" lengthAdjust="spacingAndGlyphs">DREAMS</text>
      <text class="poster-line" x="444" y="750" font-size="74" textLength="380" lengthAdjust="spacingAndGlyphs">come true</text>
    </g>

    <g class="brand">
      <circle class="brand-badge" cx="768" cy="482" r="54"/>
      <text class="brand-name" x="768" y="478" font-size="17" text-anchor="middle">RICE AND</text>
      <text class="brand-name" x="768" y="500" font-size="17" text-anchor="middle">RUN</text>
    </g>
  </g>
</svg>
</body>
</html>
```